Book Cover for Willow Kindred Notes from the Meadow

We have written a book that brings together Notes from the Meadow from a variety of women's voices.
We developed a draft book cover that we like using Canva (attached below). We'd love a book cover that is similar to this image, but looks more professional.
Following are the themes we’d like to depict in the book cover, and in parentheses, how they are represented in the current cover:
1. Divinely feminine (overall cover)
2. Currents of enlightenment (the swirls of light carrying the butterfly)
3. Diversity (a myriad of colors)
4. The solo journey into the unknown (the single butterfly’s flight)
5. Buoyancy and joy (again, the dancing colors and floating butterfly)
6. Boldly feminine (the blue butterfly, set against brush strokes of light)
7. Homage to a dear friend (she loved blue butterflies, the cosmos - this butterfly has hints of the cosmos in her wings, and painting - this background has brush strokes of light).
Book Title, Subtitle, and Editor:
Willow Kindred
Notes from the Meadow
Edited by Mirela Tove
Thank you very much for considering this project!
People who are interested in Women and Spirituality

```html
<!DOCTYPE html>
<html lang="en">
<head>
<meta charset="utf-8">
<title>Willow Kindred — Book Cover</title>
<link rel="stylesheet" href="https://fonts.googleapis.com/css2?family=Bodoni+Moda:wght@500&family=Great+Vibes&family=Lora:ital@1&display=swap">
<style>
  :root {
    --stage: #242424;
    --ink-purple: #6b2584;
    --rule-magenta: #c2338f;
    --pearl: #ece8f2;
    --lilac: #dccbea;
    --blush: #f1d3e6;
    --mint: #cfeae6;
    --butter: #f2ecc9;
    --sky: #cfe0f1;
    --wing-blue: #3a8fe0;
    --wing-deep: #1d3f72;
  }
  * { margin: 0; padding: 0; box-sizing: border-box; }
  html, body { width: 1200px; height: 800px; overflow: hidden; }
  body { background: var(--stage); position: relative; }

  .book-cover {
    position: absolute;
    left: 350px; top: 25px;
    width: 500px; height: 750px;
    overflow: hidden;
    background:
      radial-gradient(ellipse 55% 35% at 25% 30%, var(--blush) 0%, transparent 70%),
      radial-gradient(ellipse 45% 30% at 80% 45%, var(--butter) 0%, transparent 70%),
      radial-gradient(ellipse 50% 40% at 30% 70%, var(--mint) 0%, transparent 70%),
      radial-gradient(ellipse 45% 35% at 75% 85%, var(--lilac) 0%, transparent 70%),
      radial-gradient(ellipse 50% 30% at 60% 15%, var(--sky) 0%, transparent 70%),
      var(--pearl);
  }

  .cover-title {
    position: absolute;
    left: 0; top: 0;
    width: 500px; height: 280px;
  }
  .cover-title text {
    font-family: "Bodoni Moda", "Didot", serif;
    font-weight: 500;
    font-size: 138px;
    fill: var(--ink-purple);
  }

  .subtitle-band {
    position: absolute;
    left: 109px; top: 293px;
    width: 280px; height: 49px;
    border-top: 1px solid var(--rule-magenta);
    border-bottom: 1px solid var(--rule-magenta);
    display: flex; align-items: center; justify-content: center;
  }
  .subtitle {
    font-family: "Great Vibes", cursive;
    font-size: 30px;
    color: var(--ink-purple);
    white-space: nowrap;
  }

  .butterfly-art {
    position: absolute;
    left: 151px; top: 389px;
    width: 201px; height: 262px;
    border-radius: 48% 52% 40% 60% / 45% 40% 60% 55%;
    background:
      radial-gradient(ellipse at 55% 45%, var(--wing-blue) 0%, var(--wing-deep) 75%, transparent 100%);
    opacity: 0.9;
  }

  .editor-credit {
    position: absolute;
    left: 0; top: 697px;
    width: 500px;
    text-align: center;
    font-family: "Lora", Georgia, serif;
    font-style: italic;
    font-size: 23px;
    color: var(--ink-purple);
  }
</style>
</head>
<body>
  <main class="book-cover">
    <svg class="cover-title" viewBox="0 0 500 280" aria-label="Willow Kindred">
      <text x="250" y="149" text-anchor="middle" textLength="426" lengthAdjust="spacingAndGlyphs">WILLOW</text>
      <text x="266" y="259" text-anchor="middle" textLength="394" lengthAdjust="spacingAndGlyphs">KINDRED</text>
    </svg>

    <div class="subtitle-band">
      <p class="subtitle">Notes from the Meadow</p>
    </div>

    <div class="butterfly-art" role="img" aria-label="A single blue butterfly with black-veined, white-dotted wings in flight"></div>

    <p class="editor-credit">Edited by Mirela Tove</p>
  </main>
</body>
</html>
```